Book Cover Design: Manuscript Mason's™ Roadmap: Indie-Release Essentials

I need a book cover designed for the first book in the "Manuscript Mason's™ Roadmap" series. Second book to follow in a few weeks and then we'll be rolling out 1-2 new titles per month throughout 2017.

The cover design should be something that can be replicated with a new subtitle, for the next books in the series.

The graphic designer’s work that is selected for my cover series will be given credit on the copyright page of the book(s).

Target Market(s)

Authors interested in self-publishing. Publishing.

Industry/Entity Type

Publishing

Font styles to use
Serif

Requirements
Must have
• Please see attached design instructions.
Nice to have
Should not have
• Cheesy book cover images on the cover.

```html
<!DOCTYPE html>
<html lang="en">
<head>
<meta charset="utf-8">
<title>Manuscript Mason's™ Roadmap: Indie-Release Essentials — Cover Wrap</title>
<link href="https://fonts.googleapis.com/css2?family=Archivo+Narrow:wght@400;600;700&family=Playfair+Display:wght@700&family=Libre+Baskerville&display=swap" rel="stylesheet">
<style>
  :root {
    --paper: #ffffff;
    --ink: #111111;
    --slate: #3f5f6e;
    --sage: #90a89a;
    --band: #3e5d6c;
    --blueprint-light: #f4f7fb;
    --blueprint-mid: #b9cbe0;
    --blueprint-deep: #7e9cc0;
    --photo-warm: #8a3b2a;
    --photo-light: #d9b9a4;
  }
  html, body {
    margin: 0;
    padding: 0;
    width: 1200px;
    height: 886px;
    overflow: hidden;
    background: var(--paper);
  }
  .cover-wrap {
    position: relative;
    width: 1200px;
    height: 886px;
    background: var(--paper);
    font-family: "Archivo Narrow", "Arial Narrow", sans-serif;
    color: var(--ink);
  }

  /* Series title wordmark */
  .series-title {
    position: absolute;
    margin: 0;
    font-family: "Playfair Display", Georgia, serif;
    font-weight: 700;
    color: var(--slate);
    text-align: right;
    line-height: 0.9;
  }
  .series-title .series-name { display: block; }
  .series-title .series-noun { display: block; }

  .back .series-title { left: 140px; top: 62px; width: 340px; }
  .back .series-name { font-size: 34px; }
  .back .series-noun { font-size: 78px; }

  .front .series-title { left: 630px; top: 168px; width: 490px; }
  .front .series-name { font-size: 50px; }
  .front .series-noun { font-size: 116px; }

  /* Back cover */
  .back-copy {
    position: absolute;
    left: 67px;
    top: 224px;
    width: 488px;
    font-size: 13.4px;
    line-height: 24.4px;
    text-align: justify;
    hyphens: auto;
  }
  .back-copy p { margin: 0 0 24.4px; }

  .author-photo {
    position: absolute;
    left: 67px;
    top: 600px;
    width: 164px;
    height: 163px;
    background: radial-gradient(circle at 55% 45%, var(--photo-light) 0%, #b47a60 40%, var(--photo-warm) 75%, #3a2620 100%);
  }
  .author-site {
    position: absolute;
    left: 67px;
    top: 779px;
    font-size: 13.4px;
    font-weight: 700;
  }
  .publisher-name {
    position: absolute;
    left: 372px;
    top: 676px;
    width: 176px;
    font-size: 50px;
    font-weight: 400;
    line-height: 0.95;
    letter-spacing: 1px;
    color: var(--ink);
  }

  /* Spine */
  .spine {
    position: absolute;
    left: 580px;
    top: 48px;
    width: 28px;
    height: 790px;
  }
  .spine-text {
    position: absolute;
    left: 0;
    top: 0;
    writing-mode: vertical-rl;
    white-space: nowrap;
    display: flex;
    align-items: center;
    gap: 10px;
  }
  .spine-title {
    font-family: "Libre Baskerville", Georgia, serif;
    font-size: 11px;
    letter-spacing: 0.5px;
    color: var(--sage);
  }
  .spine-title strong { font-weight: 400; color: var(--slate); }
  .spine-author {
    font-size: 17px;
    letter-spacing: 4.5px;
    color: var(--ink);
  }

  /* Front cover */
  .front-author {
    position: absolute;
    left: 633px;
    top: 58px;
    margin: 0;
    font-size: 38px;
    font-weight: 400;
    letter-spacing: 5.2px;
    color: var(--ink);
  }
  .front-art {
    position: absolute;
    left: 614px;
    top: 435px;
    width: 540px;
    height: 300px;
    background: linear-gradient(180deg, var(--blueprint-light) 0%, var(--blueprint-mid) 45%, var(--blueprint-deep) 100%);
  }
  .front-band {
    position: absolute;
    left: 614px;
    top: 735px;
    width: 540px;
    height: 16px;
    background: var(--band);
  }
  .front-subtitle {
    position: absolute;
    left: 638px;
    top: 770px;
    margin: 0;
    font-size: 26px;
    font-weight: 700;
    letter-spacing: 4px;
    color: var(--ink);
  }
</style>
</head>
<body>
<main class="cover-wrap">

  <section class="back">
    <h2 class="series-title">
      <span class="series-name">Manuscript Mason's™</span>
      <span class="series-noun">Roadmap</span>
    </h2>
    <div class="back-copy">
      <p>Renata Cavendell is a leading expert in the independent publishing market, having consulted with more than 15,000 authors throughout her career as the Manuscript Mason™. A bestselling author, radio talk show host and content strategist, she has studied at the Harwick Professional Publishing program and Eastbrook State University.</p>
      <p>The Manuscript Mason's™ Roadmap: Indie-Release Essentials is a no-nonsense roadmap to publishing success for the author and small publisher alike. Both fiction and nonfiction authors will utilize this book as their publishing guide for print, e-book and audio titles. It maps the most direct route to publishing success in the most cost-effective manner, providing the indie publisher with the skills and approach of a traditional publisher and marketing strategy of a bestseller.</p>
      <p>Even if a book has already been brought to market, Manuscript Mason's™ Roadmap: Indie-Release Essentials provides pragmatic insights on how to strengthen a book's publishing, distribution and marketing foundation</p>
    </div>
    <div class="author-photo" role="img" aria-label="Author portrait photograph"></div>
    <div class="author-site">www.manuscriptmason.com</div>
    <div class="publisher-name">VELVET TIDE MEDIA</div>
  </section>

  <section class="spine">
    <div class="spine-text">
      <span class="spine-title">MANUSCRIPT MASON'S™ <strong>ROADMAP: INDIE-RELEASE ESSENTIALS</strong></span>
      <span class="spine-author">RENATA L. CAVENDELL</span>
    </div>
  </section>

  <section class="front">
    <h1 class="front-author">RENATA L. CAVENDELL</h1>
    <h2 class="series-title">
      <span class="series-name">Manuscript Mason's™</span>
      <span class="series-noun">Roadmap</span>
    </h2>
    <div class="front-art" role="img" aria-label="Photograph of architectural blueprints with a drafting compass"></div>
    <div class="front-band"></div>
    <h3 class="front-subtitle">INDIE-RELEASE ESSENTIALS</h3>
  </section>

</main>
</body>
</html>
```